Web Design Job: Facial Surgery Center (Velantra)--Web Design Needed

We need a web design for Velantra Facial Surgery. Velantra is in Chesterfield, MO (suburb of St. Louis), and is owned by a double board certified facial plastic surgeon and ENT. The website must feature a before and after photo book, a section for patient reviews, drop down menus that outline services offered (one for surgical procedures and one for office/nonsurgical procedures), and "About the Practice" section, a section to talk about the doctor and his staff, a "What's New" section, a section for information for out of town patients, as well as a link to the Medical Spa also owned by the doctor, as well as Facebook and Twitter. We are open to ideas regarding adding a "tour of the surgery center", featuring video footage of the state of the art facility, as well as other video options. We prefer soothing colors such as aquas and blues, light greys, chocolate browns, etc (does not have to follow the color scheme in the attached logo). We would like the design to be easy to digest and informative, but not "thick". It should be an upscale, classy design that will appeal to all age brackets, but especially middle-aged women, as that is the primary clientele.

Target Market(s)

Middle aged women are our most common client, however, younger patients, both male and female, will often visit the site for select procedures.

Industry/Entity Type

Medical

Number of Pages Required

5+ page

Font styles to use
Sans Serif

Colors
86cfc6
85cae6
cee9f5
cfeae6
edf8f6
85acd3
cfdfed

Requirements
Must have
• Before and after picture book, links to Facebook, Twitter and Instagram, a soothing, peaceful aesthetic, a page for reviews, as well as a link to reviews on Yelp or similar page.
Nice to have
• Drop down menus that include the surgical and nonsurgical procedures. Each surgical procedure could have it's own section that includes a before and after picture book.
Should not have
• Too many words!

```html
<!DOCTYPE html>
<html lang="en">
<head>
<meta charset="utf-8">
<title>Velantra Facial Surgery</title>
<link rel="stylesheet" href="https://fonts.googleapis.com/css2?family=Open+Sans:wght@400;600&family=Roboto+Slab:wght@300;400&display=swap">
<style>
:root{
  --blue:#2a78bf;
  --blue-deep:#1d66a8;
  --aqua:#86cfc6;
  --sky:#cee9f5;
  --mist:#edf8f6;
  --beige:#ecdfcf;
  --tan:#c8a276;
  --ink:#333;
  --muted:#777;
  --dark:#2b3640;
  --footer:#2a2a2a;
  --white:#fff;
}
*{box-sizing:border-box;margin:0;padding:0}
html,body{width:1200px;height:4376px;overflow:hidden}
body{font-family:"Open Sans",sans-serif;color:var(--ink);background:var(--white);position:relative}
.slab{font-family:"Roboto Slab",serif}
section,header,footer{position:absolute;left:0;width:1200px}
.photo{position:absolute}

/* hero */
.hero{top:0;height:660px;background:linear-gradient(90deg,#a07a5c 0%,#d7c2ae 30%,#dfe3e7 55%,#c9d1d8 100%)}
.nav{position:absolute;top:0;left:0;width:1200px;height:92px;background:rgba(255,255,255,.55);display:flex;align-items:center}
.nav a{font-size:15px;color:var(--ink);text-decoration:none;position:absolute;top:38px}
.nav a.active{color:var(--blue)}
.brand{position:absolute;left:0;width:1200px;top:10px;text-align:center;color:var(--blue);font-family:"Roboto Slab",serif;font-weight:300;pointer-events:none}
.brand .name{font-size:44px;line-height:48px;letter-spacing:1px}
.brand .sub{font-size:12px;letter-spacing:6px;text-transform:uppercase}
.hero-tag{position:absolute;right:70px;top:240px;color:var(--white);font-family:"Roboto Slab",serif;font-weight:300;text-align:right}
.hero-tag .t1{font-size:44px;color:#e9f3fa}
.hero-tag .t2{font-size:108px;line-height:130px;color:rgba(255,255,255,.75)}
.dots{position:absolute;top:606px;left:540px;display:flex;gap:10px}
.dots span{width:12px;height:12px;border-radius:50%;background:rgba(255,255,255,.6);border:1px solid #999}
.dots span.on{background:#555}

/* welcome */
.welcome{top:660px;height:400px;background:var(--white)}
.welcome h1{position:absolute;left:80px;top:50px;font-family:"Roboto Slab",serif;font-weight:400;font-size:40px;color:var(--blue)}
.welcome .swoosh{position:absolute;left:420px;top:112px}
.welcome p{position:absolute;left:80px;width:620px;font-size:14px;line-height:22px;color:var(--muted)}

/* picture book */
.book{top:1060px;height:660px;background:var(--beige)}
.book .panel-blue{position:absolute;left:0;top:0;width:400px;height:660px;background:var(--blue-deep)}
.book-cover{position:absolute;left:220px;top:160px;width:340px;height:360px;background:var(--tan);display:flex;align-items:center;justify-content:center}
.book-cover .frame{position:absolute;left:30px;top:30px;width:280px;height:300px;border:2px solid rgba(255,255,255,.6)}
.book-cover h2{font-family:"Roboto Slab",serif;font-weight:300;color:var(--white);font-size:44px;line-height:54px;text-align:center}
.book-page{position:absolute;left:560px;top:160px;width:420px;height:360px;background:var(--white);padding:44px 36px}
.ba-grid{display:grid;grid-template-columns:1fr 1fr;gap:10px;width:348px}
.ba-grid div{height:112px;background:linear-gradient(180deg,#c7a98c,#9d7b60)}
.ba-label{display:flex;justify-content:space-around;font-size:11px;letter-spacing:1px;color:var(--muted);width:348px;margin:4px 0}
.ba-caption{text-align:center;font-size:14px;color:var(--blue);width:348px;margin-top:10px}
.book-nav{position:absolute;left:1006px;top:300px;text-align:center;font-size:12px;color:var(--muted)}

/* procedures */
.procedures{top:1720px;height:660px;background:var(--white)}
.procedures h2{position:absolute;width:1200px;text-align:center;top:44px;font-family:"Roboto Slab",serif;font-weight:400;font-size:40px;color:var(--blue)}
.focus-circle{position:absolute;left:830px;top:190px;width:270px;height:270px;border-radius:50%;border:6px solid #e6ecf1;background:linear-gradient(180deg,#eadbcc,#d7bba3)}
.focus-text{position:absolute;left:820px;top:500px;width:290px;text-align:center}
.focus-text h3{font-family:"Roboto Slab",serif;font-weight:400;color:var(--blue);font-size:22px;margin-bottom:10px}
.focus-text p{font-size:12px;line-height:19px;color:var(--muted)}
.focus-text a{display:block;margin-top:8px;font-size:11px;color:var(--blue);text-decoration:none;letter-spacing:1px}

/* about */
.about{top:2380px;height:520px;background:linear-gradient(180deg,#34434e,#27323b)}
.about h2{position:absolute;width:1200px;text-align:center;top:40px;font-family:"Roboto Slab",serif;font-weight:400;font-size:40px;color:var(--white)}
.team{position:absolute;top:120px;left:80px}
.member{position:absolute;top:0;width:250px}
.member .pic{height:258px;background:linear-gradient(180deg,#b48a64,#6b4e3a);border:3px solid rgba(255,255,255,.8)}
.member .name{margin-top:12px;text-align:center;font-family:"Roboto Slab",serif;font-size:18px;color:var(--blue)}
.member .role{text-align:center;font-size:13px;color:#d7dde2}
.member .overlay{position:absolute;inset:0 0 auto 0;height:258px;background:rgba(38,110,175,.92);padding:22px 18px;color:var(--white);text-align:center;border:3px solid var(--white)}
.overlay .o-name{font-family:"Roboto Slab",serif;font-size:19px}
.overlay .o-role{font-size:12px;margin-bottom:12px}
.overlay p{font-size:11px;line-height:17px}
.overlay .socials{display:flex;justify-content:center;gap:8px;margin-top:18px}
.overlay .socials span{width:26px;height:26px;background:var(--white)}
.arrow{position:absolute}

/* reviews */
.reviews{top:2900px;height:540px;background:var(--white)}
.reviews h2{position:absolute;width:1200px;text-align:center;top:40px;font-family:"Roboto Slab",serif;font-weight:400;font-size:40px;color:var(--blue)}
.thumb{position:absolute;background:linear-gradient(180deg,#d9c4ad,#a98668)}
.quote{position:absolute;left:290px;top:380px;width:620px;text-align:center;font-size:13px;line-height:21px;color:var(--muted)}
.reviewer{position:absolute;width:1200px;text-align:center;top:462px;font-family:"Roboto Slab",serif;color:var(--blue);font-size:17px}

/* tour */
.tour{top:3440px;height:500px;background:linear-gradient(180deg,#2a3741,#41515c)}
.tour h2{position:absolute;width:1200px;text-align:center;top:44px;font-family:"Roboto Slab",serif;font-weight:400;font-size:40px;color:var(--white)}
.video{position:absolute;left:320px;top:132px;width:560px;height:328px;background:linear-gradient(180deg,#9eb5c6,#5d7585);border:4px solid rgba(255,255,255,.85)}
.video .bar{position:absolute;left:0;bottom:0;width:100%;height:34px;background:rgba(0,0,0,.55);display:flex;align-items:center;padding:0 12px;gap:12px}
.video .track{flex:1;height:4px;background:rgba(255,255,255,.4)}
.video .track i{display:block;width:30%;height:4px;background:var(--blue)}

/* badges */
.badges{top:3940px;height:148px;background:var(--white);display:flex;justify-content:space-around;align-items:center;padding:0 60px}
.badges span{width:120px;height:96px;background:#e4e8ec;border-radius:8px}
.badges span.round{width:100px;height:100px;border-radius:50%}

/* footer */
.site-footer{top:4088px;height:232px;background:var(--footer);color:#ccc}
.col{position:absolute;top:30px}
.col h4{font-weight:600;color:var(--white);font-size:16px;margin-bottom:16px}
.col .line{display:flex;gap:10px;font-size:12px;line-height:19px;margin-bottom:10px}
.tweet{font-size:12px;line-height:18px;margin-bottom:10px;display:flex;gap:10px}
.tweet em{display:block;font-style:normal;color:#888;text-align:right}
.social{display:flex;gap:14px}
.social span{width:18px;height:18px;background:#999}
.copyright{top:4320px;height:56px;background:var(--blue-deep);color:var(--white);font-size:13px;display:flex;align-items:center;justify-content:center}
</style>
</head>
<body>

<header class="hero">
  <div class="photo" role="img" aria-label="Portrait of a smiling woman with long brown hair" style="left:120px;top:0;width:520px;height:660px;background:linear-gradient(90deg,rgba(90,60,40,.0),rgba(200,160,130,.55) 40%,rgba(200,160,130,0))"></div>
  <nav class="nav">
    <a class="active" href="#" style="left:100px">Home</a>
    <a href="#" style="left:186px">Facial Procedures</a>
    <a href="#" style="left:366px">Office</a>
    <a href="#" style="left:776px">Our Practice</a>
    <a href="#" style="left:916px">Contact Us</a>
    <a href="#" style="left:1036px">Gallery</a>
  </nav>
  <div class="brand"><div class="name">velantra</div><div class="sub">Facial Surgery</div></div>
  <div class="hero-tag"><div class="t1">Experience You Can Trust</div><div class="t2">Confidence</div></div>
  <div class="dots"><span class="on"></span><span></span><span></span><span></span><span></span></div>
</header>

<section class="welcome">
  <h1>Welcome to Velantra Facial Surgery</h1>
  <svg class="swoosh" width="100" height="14" viewBox="0 0 100 14"><path d="M2 10 Q50 -2 98 8" stroke="#c8a276" stroke-width="2" fill="none"/></svg>
  <p style="top:150px">Today we find ourselves living in a health-conscious, fitness-oriented society, with an emphasis on youth and beauty. With that in mind, it is a natural for us to want to look and feel our very best.</p>
  <p style="top:226px">Our surgeon, double board certified in facial plastic surgery and ENT, has opened a new, state-of-the-art facial surgery office in Chesterfield after practicing for over fourteen years. His artistic and compassionate approach uses gentle surgical refinements such as brow, lid and neck lifts, and eyelid surgery to help each patient leave with a refreshed and rejuvenated appearance.</p>
  <div class="photo" role="img" aria-label="Woman with dark hair touching her shoulder" style="left:740px;top:12px;width:340px;height:376px;background:radial-gradient(ellipse at 55% 45%,#c9a488 0%,#e7d6c6 45%,#fff 75%)"></div>
</section>

<section class="book">
  <div class="panel-blue"></div>
  <div class="photo" role="img" aria-label="Woman peeking over the top of the picture book" style="left:440px;top:0;width:200px;height:160px;background:linear-gradient(180deg,#6b4a36,#caa688)"></div>
  <div class="book-cover"><div class="frame"></div><h2>Picture<br>Book</h2></div>
  <div class="book-page">
    <div class="ba-grid">
      <div role="img" aria-label="Patient before lower eyelid surgery, front view"></div>
      <div role="img" aria-label="Patient after lower eyelid surgery, front view"></div>
    </div>
    <div class="ba-label"><span>BEFORE</span><span>AFTER</span></div>
    <div class="ba-grid">
      <div role="img" aria-label="Patient before lower eyelid surgery, close view"></div>
      <div role="img" aria-label="Patient after lower eyelid surgery, close view"></div>
    </div>
    <div class="ba-caption">Lower Eyelid Surgery</div>
  </div>
  <div class="book-nav">
    <svg width="20" height="14" viewBox="0 0 20 14"><path d="M2 12 L10 3 L18 12" stroke="#999" stroke-width="2" fill="none"/></svg>
    <div>slide</div>
    <svg width="20" height="14" viewBox="0 0 20 14"><path d="M2 2 L10 11 L18 2" stroke="#999" stroke-width="2" fill="none"/></svg>
  </div>
</section>

<section class="procedures">
  <h2>Surgical Procedures Services</h2>
  <div class="photo" role="img" aria-label="Woman's face with treatment points marked and a syringe" style="left:300px;top:120px;width:520px;height:540px;background:radial-gradient(ellipse at 55% 45%,#d9b79a 0%,#ecdccd 45%,#fff 72%)"></div>
  <svg class="photo" style="left:560px;top:240px" width="280" height="90" viewBox="0 0 280 90"><circle cx="6" cy="6" r="6" fill="#2a78bf"/><path d="M6 6 L270 80" stroke="#b9c6d0" stroke-width="1.5"/></svg>
  <div class="focus-circle" role="img" aria-label="Woman touching her forehead"></div>
  <div class="focus-text">
    <h3>Forehead Lift</h3>
    <p>The effects of aging our foreheads, and often, the brow and forehead area show the first signs. The skin begins to lose its elasticity.</p>
    <a href="#">READ MORE ›</a>
  </div>
</section>

<section class="about">
  <h2>About the Practice</h2>
  <svg class="arrow" style="left:22px;top:250px" width="20" height="34" viewBox="0 0 20 34"><path d="M16 2 L4 17 L16 32" stroke="#fff" stroke-width="3" fill="none"/></svg>
  <svg class="arrow" style="left:1158px;top:250px" width="20" height="34" viewBox="0 0 20 34"><path d="M4 2 L16 17 L4 32" stroke="#fff" stroke-width="3" fill="none"/></svg>
  <div class="team">
    <div class="member" style="left:0"><div class="pic" role="img" aria-label="Portrait of nurse practitioner"></div><div class="name">Dana Whitfield</div><div class="role">Nurse Practitioner</div></div>
    <div class="member" style="left:260px"><div class="pic" role="img" aria-label="Portrait of patient coordinator"></div><div class="name">Grace L.</div><div class="role">Patient Coordinator</div></div>
    <div class="member" style="left:520px"><div class="pic" role="img" aria-label="Portrait of surgical coordinator"></div>
      <div class="overlay">
        <div class="o-name">Nora T.</div>
        <div class="o-role">Surgical Coordinator</div>
        <p>Nora is here to ensure a smooth flow during your appointment and can also help you navigate through the insurance maze.</p>
        <div class="socials"><span></span><span></span><span></span></div>
      </div>
    </div>
    <div class="member" style="left:784px"><div class="pic" role="img" aria-label="Portrait of medspa director"></div><div class="name">Elise R.</div><div class="role">MedSpa Director/Marketing Coordinator</div></div>
  </div>
</section>

<section class="reviews">
  <h2>Patient Reviews</h2>
  <div class="thumb" role="img" aria-label="Patient portrait" style="left:432px;top:150px;width:68px;height:96px"></div>
  <div class="thumb" role="img" aria-label="Smiling patient with light hair" style="left:500px;top:120px;width:200px;height:200px;background:linear-gradient(180deg,#e6ddd2,#b9a38c);border:4px solid #cfdfed"></div>
  <div class="thumb" role="img" aria-label="Patient portrait" style="left:700px;top:150px;width:68px;height:96px"></div>
  <svg class="arrow" style="left:230px;top:382px" width="16" height="28" viewBox="0 0 16 28"><path d="M13 2 L3 14 L13 26" stroke="#2a78bf" stroke-width="2.5" fill="none"/></svg>
  <svg class="arrow" style="left:954px;top:382px" width="16" height="28" viewBox="0 0 16 28"><path d="M3 2 L13 14 L3 26" stroke="#2a78bf" stroke-width="2.5" fill="none"/></svg>
  <p class="quote">The Doctor is very skilled at communicating well and putting me at ease with careful explanation. I was never made to feel rushed or pressured in any way. His staff is exceptionally kind and considerate of my time.</p>
  <div class="reviewer">Marina K.</div>
</section>

<section class="tour">
  <h2>Tour of the Surgery Center</h2>
  <div class="video" role="img" aria-label="Video of the operating room at the surgery center">
    <div class="bar">
      <svg width="14" height="16" viewBox="0 0 14 16"><path d="M1 1 L13 8 L1 15 Z" fill="#fff"/></svg>
      <div class="track"><i></i></div>
      <svg width="16" height="16" viewBox="0 0 16 16"><path d="M2 6 H6 L10 2 V14 L6 10 H2 Z" fill="#fff"/></svg>
      <svg width="16" height="16" viewBox="0 0 16 16"><path d="M1 5 V1 H5 M11 1 H15 V5 M15 11 V15 H11 M5 15 H1 V11" stroke="#fff" stroke-width="2" fill="none"/></svg>
    </div>
  </div>
</section>

<section class="badges">
  <span></span><span></span><span class="round"></span><span></span><span class="round"></span><span class="round"></span>
</section>

<footer class="site-footer">
  <div class="col" style="left:80px;width:300px">
    <h4>Contact Us</h4>
    <div class="line"><svg width="14" height="18" viewBox="0 0 14 18"><path d="M7 1 C3 1 1 4 1 7 C1 11 7 17 7 17 C7 17 13 11 13 7 C13 4 11 1 7 1 Z" fill="#ccc"/><circle cx="7" cy="7" r="2.2" fill="#2a2a2a"/></svg><span>2450 Linden Crest Dr, Suite 210,<br>Chesterfield, MO 63017</span></div>
    <div class="line"><svg width="14" height="16" viewBox="0 0 14 16"><path d="M3 1 L6 4 L4 7 C5 9 7 11 9 12 L12 10 L13 14 C10 16 1 8 1 3 Z" fill="#ccc"/></svg><span>314 555 0187</span></div>
    <div class="line"><svg width="16" height="12" viewBox="0 0 16 12"><rect x="1" y="1" width="14" height="10" fill="none" stroke="#ccc" stroke-width="1.5"/><path d="M1 1 L8 7 L15 1" stroke="#ccc" stroke-width="1.5" fill="none"/></svg><span>hello@velantrafacial.com</span></div>
  </div>
  <div class="col" style="left:432px;width:320px">
    <h4>RECENT TWEETS</h4>
    <div class="tweet"><svg width="16" height="14" viewBox="0 0 16 14"><rect width="16" height="14" rx="3" fill="#888"/></svg><span>New patient hours now open on Saturdays, book your visit with our friendly team today.<em>4 days ago</em></span></div>
    <div class="tweet"><svg width="16" height="14" viewBox="0 0 16 14"><rect width="16" height="14" rx="3" fill="#888"/></svg><span>See our latest before and after gallery. This post is new!<em>4 days ago</em></span></div>
  </div>
  <div class="col" style="left:792px;width:320px">
    <h4>Social Links</h4>
    <div class="social"><span></span><span></span><span></span><span></span><span></span><span></span><span></span></div>
  </div>
</footer>
<div class="copyright" style="position:absolute;left:0;width:1200px;top:4320px">© 2024 Velantra Facial Surgery. All Rights Reserved.</div>

</body>
</html>
```